Brasko Construction Business Card

I need a business card design for my company.
We are a construction/machinery company.
I would like to see my logo on the front of the card and my details on the other side
I would like the card to be black or dark grey in colour,with my logo as i send it or modified with a lighter blue colour
I would like to see the design kept fairly simple,but eye catching at the same time
Industry/Entity Type
Business
Contact Information for Business Card
Name
Phone Number
Address
Email
Colors
00a990
1b1b1b
000000
474747
ececec

```html
<!DOCTYPE html>
<html lang="en">
<head>
<meta charset="utf-8">
<title>Brasko Construction Business Card</title>
<link rel="stylesheet" href="https://fonts.googleapis.com/css2?family=Open+Sans:wght@400;600;700&display=swap">
<style>
  :root {
    --brand-teal: #00a990;
    --charcoal: #474747;
    --ink: #1b1b1b;
    --paper: #ececec;
    --white: #ffffff;
  }
  * { margin: 0; padding: 0; box-sizing: border-box; }
  html, body { width: 1200px; height: 900px; overflow: hidden; }
  body {
    background: var(--paper);
    font-family: "Open Sans", sans-serif;
    position: relative;
  }
  .card {
    position: absolute;
    width: 556px;
    height: 343px;
    box-shadow: 0 6px 18px rgba(0,0,0,0.18);
    overflow: hidden;
  }

  /* Details side */
  .card-details {
    left: 238px;
    top: 62px;
    background: var(--brand-teal);
    color: var(--white);
  }
  .artwork {
    position: absolute;
    left: 0;
    top: 0;
    width: 320px;
    height: 343px;
    background: linear-gradient(160deg, var(--brand-teal) 0%, #2f8a7c 40%, var(--charcoal) 72%);
  }
  .details-block {
    position: absolute;
    right: 34px;
    top: 34px;
    text-align: right;
  }
  .company-name {
    font-weight: 700;
    text-transform: uppercase;
    line-height: 1;
    margin-bottom: 28px;
  }
  .company-name .word-main {
    display: block;
    font-size: 38px;
    letter-spacing: 1px;
  }
  .company-name .word-sub {
    display: block;
    font-size: 17px;
    letter-spacing: 3.4px;
    margin-top: 4px;
    margin-right: -3px;
  }
  .person-name {
    font-size: 18px;
    font-weight: 600;
    line-height: 22px;
  }
  .person-role {
    font-size: 14px;
    line-height: 20px;
    margin-bottom: 22px;
  }
  .contact-line {
    font-size: 14px;
    line-height: 21px;
    display: flex;
    justify-content: flex-end;
    align-items: center;
    gap: 10px;
  }
  .contact-line svg { width: 10px; height: 10px; fill: var(--white); }
  .address {
    font-size: 14px;
    line-height: 20px;
    margin-top: 21px;
  }

  /* Brand side */
  .card-brand {
    left: 458px;
    top: 518px;
    width: 560px;
    background: var(--charcoal);
  }
  .brand-name {
    position: absolute;
    left: 0;
    right: 0;
    top: 184px;
    text-align: center;
    color: var(--brand-teal);
    font-weight: 700;
    text-transform: uppercase;
    line-height: 1;
  }
  .brand-name .word-main {
    display: block;
    font-size: 50px;
    letter-spacing: 2px;
  }
  .brand-name .word-sub {
    display: block;
    font-size: 24px;
    letter-spacing: 5px;
    margin-top: 6px;
  }
</style>
</head>
<body>
  <section class="card card-details">
    <div class="artwork" role="img" aria-label="Illustration of an excavator arm and bucket digging into dark ground"></div>
    <div class="details-block">
      <div class="company-name">
        <span class="word-main">Brasko</span>
        <span class="word-sub">Construction</span>
      </div>
      <div class="person-name">Daniel Mercer</div>
      <div class="person-role">Managing Director</div>
      <div class="contact-line">044-987 650 312
        <svg viewBox="0 0 24 24" aria-hidden="true"><path d="M6.6 10.8a15 15 0 0 0 6.6 6.6l2.2-2.2a1 1 0 0 1 1-.25 11.4 11.4 0 0 0 3.6.57 1 1 0 0 1 1 1V20a1 1 0 0 1-1 1A17 17 0 0 1 3 4a1 1 0 0 1 1-1h3.5a1 1 0 0 1 1 1c0 1.25.2 2.45.57 3.57a1 1 0 0 1-.25 1z"/></svg>
      </div>
      <div class="contact-line">info@braskobuild.com
        <svg viewBox="0 0 24 24" aria-hidden="true"><path d="M2 5h20v14H2z" fill="var(--white)"/><path d="M2 5l10 8 10-8" fill="none" stroke="var(--brand-teal)" stroke-width="2"/></svg>
      </div>
      <div class="address">48 Harbour Lane, Unit 7<br>Eastbrook, Norvale 2041.</div>
    </div>
  </section>

  <section class="card card-brand">
    <div class="brand-name">
      <span class="word-main">Brasko</span>
      <span class="word-sub">Construction</span>
    </div>
  </section>
</body>
</html>
```